Minimalist theatrical poster for the film

Create a poster, using some of the attached images for inspiration. Please match the font of the teaser poster for the title (The Bluewater) and leave space at the bottom for the credits block, which I will add later. Any characters presented on the poster should resemble the actors in the film, and not be clip art. The movie is about Owen, a 14 year old in the summer of 2001, and his first love (Greta). As he falls for her, he lets himself still be distracted by his good friend Maisie, eventually causing trouble in his relationships with Greta, Maisie, and best friend Theo. Trailer is included in the files below! Extra credit for a good marketing tag along the lines of "remember your first love" or something about the film being a romantic comedy adventure etc.

```html
<!DOCTYPE html>
<html lang="en">
<head>
<meta charset="utf-8">
<title>Owen and the Lanterns – Poster</title>
<link href="https://fonts.googleapis.com/css2?family=Amatic+SC:wght@400;700&display=swap" rel="stylesheet">
<style>
  :root {
    --page: #ffffff;
    --coral: #f4504a;
    --coral-light: #ff8a80;
    --red-deep: #dc2a27;
    --title: #8c1b22;
    --title-soft: #fbe0dc;
    --tagline: #ffffff;
    --photo-sky: #8fb27a;
    --photo-shade: #5b6b48;
    --photo-ground: #b9a48a;
  }
  html, body {
    margin: 0;
    width: 1200px;
    height: 1200px;
    overflow: hidden;
    background: var(--page);
  }
  .poster {
    position: absolute;
    left: 343px;
    top: 218px;
    width: 501px;
    height: 751px;
    overflow: hidden;
    background:
      radial-gradient(ellipse 170px 150px at 30px 120px, rgba(255,220,215,0.75), rgba(255,220,215,0) 100%),
      radial-gradient(ellipse 260px 230px at 250px 420px, rgba(255,205,195,0.55), rgba(255,205,195,0) 100%),
      linear-gradient(90deg, rgba(220,42,39,0) 70%, var(--red-deep) 100%),
      linear-gradient(180deg, var(--coral-light) 0%, var(--coral) 45%, #f2433f 100%);
  }
  .title {
    position: absolute;
    left: 0;
    top: 0;
    width: 100%;
    height: 290px;
    margin: 0;
    font-family: "Amatic SC", sans-serif;
    font-weight: 700;
  }
  .title span {
    position: absolute;
    left: 100px;
    width: 300px;
    text-align: center;
    line-height: 1;
    white-space: nowrap;
  }
  .title-name {
    top: 22px;
    font-size: 132px;
    color: var(--title);
  }
  .title-joiner {
    top: 146px;
    font-size: 40px;
    color: var(--title-soft);
    letter-spacing: 2px;
  }
  .title-word {
    top: 180px;
    font-size: 100px;
    color: var(--title);
  }
  .heart {
    position: absolute;
    left: 78px;
    top: 290px;
    width: 346px;
    height: 270px;
    filter: drop-shadow(0 0 18px rgba(255,225,220,0.9));
  }
  .tagline {
    position: absolute;
    left: 0;
    top: 488px;
    width: 100%;
    margin: 0;
    text-align: center;
    font-family: "Amatic SC", sans-serif;
    font-weight: 400;
    font-size: 52px;
    line-height: 42px;
    letter-spacing: 1px;
    text-transform: uppercase;
    color: var(--tagline);
    text-shadow: 0 0 4px rgba(120,30,30,0.35);
  }
</style>
</head>
<body>
  <main class="poster">
    <h1 class="title">
      <span class="title-name">Owen</span>
      <span class="title-joiner">and the</span>
      <span class="title-word">Lanterns</span>
    </h1>

    <svg class="heart" viewBox="0 0 346 270" role="img" aria-label="Photo of two teenagers on park swings holding hands, trees and picnic shelter behind">
      <defs>
        <linearGradient id="park-scene" x1="0" y1="0" x2="0" y2="1">
          <stop offset="0" stop-color="var(--photo-sky)"/>
          <stop offset="0.35" stop-color="var(--photo-shade)"/>
          <stop offset="0.55" stop-color="#c9bfae"/>
          <stop offset="1" stop-color="var(--photo-ground)"/>
        </linearGradient>
      </defs>
      <path d="M173 48 C150 12 118 0 85 0 C35 0 0 38 0 88 C0 160 100 220 173 270 C246 220 346 160 346 88 C346 38 311 0 261 0 C228 0 196 12 173 48 Z" fill="url(#park-scene)"/>
    </svg>

    <p class="tagline">There is nothing in life<br>as memorable, touching,<br>tenuous, and heartbreaking<br>as that very first love</p>
  </main>
</body>
</html>
```